Township of Harlowden E-Alert Signup

Need to create print media that is designed for a Town in New Jersey that is starting a marketing campaign to get townspeople to sign up for the E-Alert system.Need print media that is 1. interchangeable in size (regular letter-size, as well as a poster size) 2. Branded with their colors, logo, etc. (green and white displayed in logo)3. Displays the incentives to sign up. Incentives:- Community Services/Announcements- Gov’t/Non-profit Resources- Tax Information- Employment opportunities- Municipal Services/Public Works/Recreation Divisions- Health Updates
Target Market(s)
Townspeople of Maplewood NJ
Industry/Entity Type
Government
Colors
Designer to choose colors to be used in the design.
Requirements
Must have
- 1. interchangeable in size (regular letter-size, as well as a poster size)
- 2. Branded with their colors, logo, etc. (green and white displayed in logo)
- 3. Displays the incentives to sign up.
- Incentives:
- - Community Services/Announcements
- - Gov’t/Non-profit Resources
- - Tax Information
- - Employment opportunities
- - Municipal Services/Public Works/Recreation Divisions
- - Health Updates

```html
<!DOCTYPE html>
<html lang="en">
<head>
<meta charset="UTF-8">
<title>Township of Harlowden E-Alert Signup</title>
<link rel="stylesheet" href="https://fonts.googleapis.com/css2?family=Archivo+Black&family=Archivo:wght@800;900&display=swap">
<style>
  :root {
    --green: #117e40;
    --red: #ec1f27;
    --white: #ffffff;
    --yellow: #f7ec1b;
    --sky: #4f6fb4;
    --brick: #8a7466;
    --road: #6d6a66;
  }
  * { margin: 0; padding: 0; box-sizing: border-box; }
  html, body { width: 1200px; height: 1200px; overflow: hidden; background: var(--white); }
  .poster {
    position: absolute; left: 274px; top: 139px;
    width: 652px; height: 923px;
    background: var(--green);
    overflow: hidden;
    font-family: "Archivo", "Arial Black", sans-serif;
  }
  .top-band { position: absolute; left: 0; top: 0; width: 100%; height: 124px; background: var(--green); }
  .township {
    position: absolute; left: 34px; top: 92px;
    color: var(--white); font-weight: 900; font-size: 20px; letter-spacing: 4.2px;
    text-transform: uppercase; line-height: 1;
  }
  .title-band { position: absolute; left: 0; top: 124px; width: 100%; height: 242px; background: var(--red); }
  .title {
    position: absolute; left: 34px; top: 152px;
    color: var(--white); font-family: "Archivo Black", "Arial Black", sans-serif;
    font-size: 100px; line-height: 84px; letter-spacing: -4px;
  }
  .seal {
    position: absolute; left: 427px; top: 33px; width: 194px; height: 194px;
    border-radius: 50%; background: var(--white);
    display: flex; align-items: center; justify-content: center;
    color: var(--green); font-weight: 900; font-size: 24px; letter-spacing: 1px;
  }
  .town-photo {
    position: absolute; left: 0; top: 366px; width: 100%; height: 303px;
    background: linear-gradient(180deg, var(--sky) 0%, #7f92c2 28%, #c9b9a3 42%, var(--brick) 62%, #4a3f38 80%, var(--road) 100%);
  }
  .alerts-heading {
    position: absolute; left: 0; top: 688px; width: 100%;
    text-align: center; padding-left: 16px;
    color: var(--yellow); font-family: "Archivo Black", "Arial Black", sans-serif;
    font-size: 54px; line-height: 1; letter-spacing: -1.5px;
  }
  .benefits { position: absolute; top: 750px; list-style: none; }
  .benefits.left { left: 82px; }
  .benefits.right { left: 337px; }
  .benefits li {
    position: relative; padding-left: 28px;
    color: var(--white); font-weight: 800; font-size: 18.5px; line-height: 24px;
  }
  .benefits li svg { position: absolute; left: 0; top: 3px; width: 18px; height: 18px; }
  .web {
    position: absolute; left: 349px; top: 884px;
    color: var(--yellow); font-weight: 900; font-size: 11px; letter-spacing: 3.4px;
  }
</style>
</head>
<body>
<main class="poster">
  <div class="top-band"></div>
  <div class="title-band"></div>
  <p class="township">Township of Harlowden</p>
  <h1 class="title">E-Alert<br>SIGNUP</h1>
  <div class="seal">HARLOWDEN</div>
  <div class="town-photo" role="img" aria-label="Photo of the town's downtown street with shops, trees and parked cars under a blue sky"></div>
  <h2 class="alerts-heading">GET ALERTS ON;</h2>
  <ul class="benefits left">
    <li><svg viewBox="0 0 18 18"><rect x="1.5" y="3" width="13" height="13" fill="none" stroke="#fff" stroke-width="2"/><path d="M4.5 9l3.5 3.5L16.5 2" fill="none" stroke="#fff" stroke-width="2.4"/></svg>Community Services<br>/Announcements</li>
    <li><svg viewBox="0 0 18 18"><rect x="1.5" y="3" width="13" height="13" fill="none" stroke="#fff" stroke-width="2"/><path d="M4.5 9l3.5 3.5L16.5 2" fill="none" stroke="#fff" stroke-width="2.4"/></svg>Gov’t/Non-profit<br>Resources</li>
    <li><svg viewBox="0 0 18 18"><rect x="1.5" y="3" width="13" height="13" fill="none" stroke="#fff" stroke-width="2"/><path d="M4.5 9l3.5 3.5L16.5 2" fill="none" stroke="#fff" stroke-width="2.4"/></svg>Tax Information</li>
    <li><svg viewBox="0 0 18 18"><rect x="1.5" y="3" width="13" height="13" fill="none" stroke="#fff" stroke-width="2"/><path d="M4.5 9l3.5 3.5L16.5 2" fill="none" stroke="#fff" stroke-width="2.4"/></svg>Employment<br>opportunities</li>
  </ul>
  <ul class="benefits right">
    <li><svg viewBox="0 0 18 18"><rect x="1.5" y="3" width="13" height="13" fill="none" stroke="#fff" stroke-width="2"/><path d="M4.5 9l3.5 3.5L16.5 2" fill="none" stroke="#fff" stroke-width="2.4"/></svg>Municipal Services<br>/Public Works/<br>Recreation Divisions</li>
    <li><svg viewBox="0 0 18 18"><rect x="1.5" y="3" width="13" height="13" fill="none" stroke="#fff" stroke-width="2"/><path d="M4.5 9l3.5 3.5L16.5 2" fill="none" stroke="#fff" stroke-width="2.4"/></svg>Health Updates</li>
  </ul>
  <p class="web">TWP.HARLOWDEN.NJ.US</p>
</main>
</body>
</html>
```